Breezeway Climate Business Card Design

Design new, 2 sides, business cards for a residential and light commercial heating, air conditioning contractor.

Target Market(s)

Homeowners, small businesses

Industry/Entity Type

Business

Contact Information for Business Card

Dominic Vasquerelli
Phone - 555-214-6837
Email
Address - PO box 618
Millbrook NJ 07999
Website - www.BreezewayClimateLLC.example

Requirements
Must have
• logo, company colors, standard size with no die cut, so I can use printhaven

```html
<!DOCTYPE html>
<html lang="en">
<head>
<meta charset="utf-8">
<title>Breezeway Climate Business Card</title>
<link href="https://fonts.googleapis.com/css2?family=Lato:wght@400;700&display=swap" rel="stylesheet">
<style>
  :root {
    --maroon: #9b2335;
    --orange: #f39420;
    --ink: #5a5a5a;
    --paper: #ffffff;
    --backdrop: #e9e9ea;
  }
  * { box-sizing: border-box; margin: 0; padding: 0; }
  html, body { width: 1200px; height: 814px; overflow: hidden; }
  body {
    background: var(--backdrop);
    font-family: "Lato", sans-serif;
    position: relative;
  }
  .card {
    position: absolute;
    top: 258px;
    width: 520px;
    height: 297px;
    box-shadow: 0 6px 18px rgba(0,0,0,.18);
    overflow: hidden;
  }
  .card-back { left: 60px; background: var(--maroon); }
  .card-front { left: 620px; background: var(--paper); }

  .brand {
    display: flex;
    align-items: center;
    gap: 8px;
    color: var(--orange);
    font-weight: 700;
    white-space: nowrap;
  }
  .brand-dot {
    width: 14px; height: 14px; border-radius: 50%;
    background: var(--orange);
  }
  .card-back .brand {
    position: absolute;
    left: 0; right: 0; top: 100px;
    justify-content: center;
    font-size: 30px;
  }
  .card-back .website {
    position: absolute;
    left: 0; right: 0; bottom: 38px;
    text-align: center;
    color: #fff;
    font-size: 14px;
  }

  .swoosh { position: absolute; inset: 0; }
  .card-front .brand {
    position: absolute;
    right: 26px; top: 44px;
    font-size: 20px;
    color: var(--maroon);
  }
  .card-front .brand-dot { background: var(--maroon); }
  .holder {
    position: absolute;
    left: 34px; top: 118px;
    color: var(--orange);
    font-weight: 700;
    font-size: 22px;
  }
  .contacts {
    position: absolute;
    left: 34px; top: 160px;
    list-style: none;
    color: var(--ink);
    font-size: 13.5px;
    line-height: 20px;
  }
  .contacts li { display: flex; gap: 10px; align-items: flex-start; }
  .contacts .icon { width: 13px; height: 20px; flex: none; }
  .contacts .address { margin-top: 10px; }
</style>
</head>
<body>
  <section class="card card-back" aria-label="Card back">
    <div class="brand"><span class="brand-dot"></span>Breezeway Climate</div>
    <p class="website">www.BreezewayClimateLLC.example</p>
  </section>

  <section class="card card-front" aria-label="Card front">
    <svg class="swoosh" viewBox="0 0 520 297" preserveAspectRatio="none" aria-hidden="true">
      <path d="M520 70 L520 297 L250 297 C340 240 420 150 520 70 Z" fill="var(--orange)"/>
      <path d="M520 82 L520 297 L275 297 C360 245 440 160 520 82 Z" fill="#fff"/>
      <path d="M520 90 L520 297 L290 297 C370 248 448 168 520 90 Z" fill="var(--maroon)"/>
    </svg>
    <div class="brand"><span class="brand-dot"></span>Breezeway Climate</div>
    <h1 class="holder">Dominic Vasquerelli</h1>
    <ul class="contacts">
      <li>
        <svg class="icon" viewBox="0 0 13 20"><path d="M3 5 L5 5 L6 8 L5 9 C6 11 7 12 8.5 13 L9.5 12 L12 13 L12 15 C7 16 2 10 3 5 Z" fill="var(--maroon)"/></svg>
        <span>555-214-6837</span>
      </li>
      <li>
        <svg class="icon" viewBox="0 0 13 20"><rect x="1" y="6" width="11" height="8" fill="var(--maroon)"/><path d="M1 6 L6.5 11 L12 6" stroke="#fff" fill="none"/></svg>
        <span>info@BreezewayClimateLLC.example</span>
      </li>
      <li>
        <svg class="icon" viewBox="0 0 13 20"><circle cx="6.5" cy="10" r="5" fill="none" stroke="var(--maroon)"/><path d="M1.5 10 H11.5 M6.5 5 V15" stroke="var(--maroon)"/></svg>
        <span>www.BreezewayClimateLLC.example</span>
      </li>
      <li class="address">
        <svg class="icon" viewBox="0 0 13 20"><path d="M6.5 17 C3 12 2 10 2 8 A4.5 4.5 0 0 1 11 8 C11 10 10 12 6.5 17 Z" fill="var(--orange)"/><circle cx="6.5" cy="8" r="1.6" fill="#fff"/></svg>
        <span>PO box 618<br>Millbrook NJ 07999</span>
      </li>
    </ul>
  </section>
</body>
</html>
```